Business card design for new, innovative company - BluePlinth

We are a new company looking for a business card design that is fun, different and quirky. Must use corporate colour green - CMYK C:55, M:0, Y:100, K:0, and corporate colour grey - C:0, M:0, Y: 0, K:70.

We have developed the first real time data application, in which people are able to profile the data of their existing customers in order to pull out more good fit clients to direct their marketing activities at.

Industry/Entity Type

Marketing

Requirements
Must have
• Logo, name, title, telephone number, fax number, email, website, address

```html
<!DOCTYPE html>
<html lang="en">
<head>
<meta charset="utf-8">
<title>BluePlinth Business Card</title>
<link rel="stylesheet" href="https://fonts.googleapis.com/css2?family=Roboto+Condensed:wght@400;700&display=swap">
<style>
  :root {
    --brand-green: #83bd27;
    --brand-grey: #6d6e70;
    --paper-white: #ffffff;
    --backdrop: #eeeeee;
    --contact-text: #f2f2f2;
  }
  * { margin: 0; padding: 0; box-sizing: border-box; }
  html, body {
    width: 1200px;
    height: 849px;
    overflow: hidden;
    background: var(--backdrop);
    font-family: "Roboto Condensed", "Arial Narrow", sans-serif;
  }
  .canvas {
    position: relative;
    width: 1200px;
    height: 849px;
  }
  .card {
    position: absolute;
    top: 302px;
    width: 242px;
    height: 242px;
  }
  .card-front {
    left: 322px;
    background: var(--brand-green);
    display: flex;
    align-items: center;
    justify-content: center;
  }
  .brand-name {
    color: var(--paper-white);
    font-weight: 700;
    font-size: 36px;
    letter-spacing: -0.5px;
  }
  .card-back {
    left: 636px;
    background: var(--brand-grey);
  }
  .person-name {
    position: absolute;
    left: 31px;
    top: 56px;
    color: var(--brand-green);
    font-weight: 700;
    font-size: 21px;
    letter-spacing: 0.6px;
    text-transform: uppercase;
  }
  .contact-line {
    position: absolute;
    left: 31px;
    display: flex;
    align-items: flex-start;
    color: var(--contact-text);
    font-size: 11px;
    line-height: 16px;
    white-space: nowrap;
  }
  .contact-icon {
    width: 11px;
    height: 11px;
    margin-top: 2px;
    margin-right: 6px;
    flex: none;
    fill: none;
    stroke: var(--brand-green);
    stroke-width: 1.4;
  }
  .contact-icon.solid { fill: var(--brand-green); stroke: none; }
  .phone-pair .secondary { margin-left: 13px; display: flex; }
  .line-phone { top: 98px; }
  .line-email { top: 120px; }
  .line-web { top: 142px; }
  .line-address { top: 164px; }
</style>
</head>
<body>
<main class="canvas">
  <section class="card card-front">
    <span class="brand-name">BluePlinth</span>
  </section>

  <section class="card card-back">
    <h1 class="person-name">Dana Whitfield</h1>

    <div class="contact-line line-phone phone-pair">
      <svg class="contact-icon" viewBox="0 0 12 12" aria-hidden="true"><rect x="3" y="0.8" width="6" height="10.4" rx="1"/><line x1="5" y1="9.3" x2="7" y2="9.3"/></svg>
      <span>07700900418</span>
      <span class="secondary">
        <svg class="contact-icon" viewBox="0 0 12 12" aria-hidden="true"><path d="M3 1 L5 3.5 L4 5 Q5.5 7.5 7 8 L8.5 7 L11 9 L9.5 11 Q4 10 1 3 Z"/></svg>
        <span>01632 960274</span>
      </span>
    </div>

    <div class="contact-line line-email">
      <svg class="contact-icon" viewBox="0 0 12 12" aria-hidden="true"><rect x="0.8" y="2.5" width="10.4" height="7"/><polyline points="0.8,2.5 6,6.5 11.2,2.5"/></svg>
      <span>dana.whitfield@blueplinth.com</span>
    </div>

    <div class="contact-line line-web">
      <svg class="contact-icon solid" viewBox="0 0 12 12" aria-hidden="true"><circle cx="6" cy="6" r="5.2"/></svg>
      <span>www.blueplinth.com</span>
    </div>

    <div class="contact-line line-address">
      <svg class="contact-icon" viewBox="0 0 12 12" aria-hidden="true"><path d="M6 11.4 C3 7.6 2 6 2 4.4 A4 4 0 0 1 10 4.4 C10 6 9 7.6 6 11.4 Z"/><circle cx="6" cy="4.4" r="1.4"/></svg>
      <span>12a Fenbrook Road, Elmsford,<br>Northshire, NS14 2QL</span>
    </div>
  </section>
</main>
</body>
</html>
```